Harborline Restoration Business Card Design Phase 2

Professional and clean design. The design colors should flow with the logo. Two-sided card with the website on the back which is:

www.HarborlineRestoration.example.

"Specializing in Water Damage Restoration"

On the front I need the name, email, phone, and logo.

Name: Darnell Vickery
Email: Darnell@HarborlineRestoration.example
Phone: 555-018-2734 for now

I only have the Preview and Thumbnail right now but should have the source files uploaded within a day or two.

Target Market(s)

Flood victims, home owners with water damage from busted pipes etc...

Industry/Entity Type

Business

Contact Information for Business Card

Name: Darnell Vickery

Font styles to use
Serif
Sans Serif

Requirements
Must have
• Business Card Details Info

```html
<!DOCTYPE html>
<html lang="en">
<head>
<meta charset="utf-8">
<title>Harborline Restoration — Business Card</title>
<link rel="stylesheet" href="https://fonts.googleapis.com/css2?family=Oswald:wght@700&family=Open+Sans:wght@400;700&family=Cinzel:wght@400&display=swap">
<style>
  :root {
    --navy: #1e3663;
    --green: #4a8f3a;
    --white: #ffffff;
    --backdrop: #e9eaec;
  }
  * { box-sizing: border-box; margin: 0; padding: 0; }
  html, body {
    width: 1200px; height: 900px; overflow: hidden;
    background: var(--backdrop);
    font-family: "Open Sans", Arial, sans-serif;
  }
  .card {
    position: absolute;
    left: 250px;
    width: 700px; height: 400px;
    background: var(--white);
    box-shadow: 0 6px 20px rgba(0,0,0,0.18);
    overflow: hidden;
  }
  .card--back { top: 35px; }
  .card--front { top: 465px; }

  .wordmark {
    font-family: "Oswald", "Arial Narrow", sans-serif;
    font-weight: 700;
    color: var(--navy);
    text-transform: uppercase;
    line-height: 0.95;
    letter-spacing: 1px;
  }

  /* back side */
  .back-content {
    position: absolute; inset: 0;
    display: flex; flex-direction: column;
    align-items: center; justify-content: center;
    text-align: center;
  }
  .back-content .wordmark { font-size: 64px; }
  .tagline {
    margin-top: 26px;
    font-family: "Cinzel", Georgia, serif;
    font-size: 15px;
    letter-spacing: 1.5px;
    color: var(--navy);
  }
  .back-website {
    margin-top: 6px;
    font-size: 17px;
    color: var(--navy);
  }

  /* front side */
  .front-logo {
    position: absolute;
    left: 0; top: 0; width: 300px; height: 100%;
    display: flex; align-items: center; justify-content: center;
  }
  .front-logo .wordmark { font-size: 42px; text-align: center; }
  .divider {
    position: absolute; left: 304px; top: 0;
    width: 5px; height: 100%;
    background: var(--green);
  }
  .contact-panel {
    position: absolute; left: 316px; top: 0; right: 0; bottom: 0;
    background: var(--navy);
    padding: 62px 32px 0 24px;
    text-align: right;
    color: var(--white);
  }
  .person-name {
    font-size: 24px; font-weight: 700;
    letter-spacing: 0.5px;
    text-transform: uppercase;
    white-space: nowrap;
  }
  .person-name .first { color: var(--green); }
  .contact-list { list-style: none; margin-top: 18px; }
  .contact-list li {
    display: flex; justify-content: flex-end; align-items: center;
    gap: 10px;
    font-size: 15px; line-height: 1.5;
    white-space: nowrap;
  }
  .contact-list svg { width: 12px; height: 12px; flex: none; }
</style>
</head>
<body>

<section class="card card--back" aria-label="Card back">
  <div class="back-content">
    <div class="wordmark">Harborline<br>Restoration</div>
    <p class="tagline">SPECIALIZING IN WATER DAMAGE RESTORATION</p>
    <p class="back-website">www.HarborlineRestoration.example</p>
  </div>
</section>

<section class="card card--front" aria-label="Card front">
  <div class="front-logo">
    <div class="wordmark">Harborline<br>Restoration</div>
  </div>
  <div class="divider"></div>
  <div class="contact-panel">
    <p class="person-name"><span class="first">Darnell</span> Vickery</p>
    <ul class="contact-list">
      <li>555-018-2734
        <svg viewBox="0 0 24 24" aria-hidden="true"><path fill="#4a8f3a" d="M6.6 10.8a15 15 0 0 0 6.6 6.6l2.2-2.2a1 1 0 0 1 1-.25 11.4 11.4 0 0 0 3.6.57 1 1 0 0 1 1 1V20a1 1 0 0 1-1 1A17 17 0 0 1 3 4a1 1 0 0 1 1-1h3.5a1 1 0 0 1 1 1c0 1.25.2 2.45.57 3.6a1 1 0 0 1-.25 1z"/></svg>
      </li>
      <li>Darnell@HarborlineRestoration.example
        <svg viewBox="0 0 24 24" aria-hidden="true"><rect x="2" y="5" width="20" height="14" rx="1.5" fill="none" stroke="#4a8f3a" stroke-width="2.4"/><path d="M3 6l9 7 9-7" fill="none" stroke="#4a8f3a" stroke-width="2.4"/></svg>
      </li>
      <li>www.HarborlineRestoration.example
        <svg viewBox="0 0 24 24" aria-hidden="true"><circle cx="12" cy="12" r="9.5" fill="none" stroke="#4a8f3a" stroke-width="2.4"/><ellipse cx="12" cy="12" rx="4" ry="9.5" fill="none" stroke="#4a8f3a" stroke-width="2"/><path d="M2.5 12h19" stroke="#4a8f3a" stroke-width="2"/></svg>
      </li>
    </ul>
  </div>
</section>

</body>
</html>
```